Non-profit organization needs newsletter

We are a non-profit organization that conducts medical missions overseas. We recently returned from a mission to Guangaje and Latacunga, Ecuador and need a newsletter describing our work to our supporters. We have a logo and would like the design to include the blue, green and white of the logo as well. The final design should be professional and communicate the culture of Ecuador using the photos of the people we helped and their corresponding stories
Updates

Reason: I NEED SOME SMALL CHANGES TO SOME DESIGN.

Target Market(s)

Prospective donors to our organization

Industry/Entity Type

Non Profit

Font styles to use
Sans Serif

Colors
9bcb3c
0456a4

Requirements
Must have
• 2 page newsletter, logo must be on the front page. Front page must feature pictures of the village of Guangaje and the text description. Front page must have the words GLOBAL VOLUNTEERISM COMPASSION ALTRUISM across the top of the page. Bottom of front page must have text that thanks donors for their support. Back page must have website address along the bottom. New hospital picture and text must be on back page. Pictures of patients and the corresponding text should be on the bottom of front page and also on the back page. Color theme is same colors in logo
Nice to have
• Pictures of random people can be untitled and just scattered throughout the newsletter.
Should not have
• Techno or modern design or non traditional font.

```html
<!DOCTYPE html>
<html lang="en">
<head>
<meta charset="utf-8">
<title>Cumbre Medical Missions — Mission Newsletter</title>
<link href="https://fonts.googleapis.com/css2?family=Didact+Gothic&family=Roboto+Condensed:wght@400;700&display=swap" rel="stylesheet">
<style>
:root{
  --sky:#75b9e6;
  --blue:#0456a4;
  --green:#9bcb3c;
  --tint:#f3f9e6;
  --rule:#dcebc2;
  --ink:#2a2a2a;
  --white:#ffffff;
}
*{margin:0;padding:0;box-sizing:border-box}
html,body{width:1170px;height:1200px;overflow:hidden;background:var(--sky)}
body{position:relative;font-family:"Didact Gothic",sans-serif;color:var(--ink)}
.page{position:absolute;top:98px;width:498px;height:1008px;background:var(--white)}
.page--front{left:74px}
.page--back{left:604px}
.abs{position:absolute}
.heading{font-family:"Roboto Condensed",sans-serif;font-weight:700;color:var(--blue);font-size:11.5px;letter-spacing:.1px}
.rule{position:absolute;height:3px;background:var(--green)}
.body-copy{font-size:10.4px;line-height:15.3px;letter-spacing:.6px}
.photo{position:absolute;overflow:hidden}
.photo-frame{position:absolute;border:1.5px solid var(--white)}
.green-block{position:absolute;background:var(--green)}

/* masthead */
.brand{left:24px;top:40px;width:150px;text-align:center}
.brand-mark{width:38px;height:38px;border-radius:50%;background:var(--blue);margin:0 auto 10px}
.brand-name{font-family:"Roboto Condensed",sans-serif;font-weight:700;color:var(--blue);font-size:13px;line-height:15px;letter-spacing:.6px}
.date-box{left:393px;top:26px;width:82px;height:82px;background:var(--blue);color:var(--white);text-align:center;font-family:"Roboto Condensed",sans-serif;font-weight:700}
.date-box svg{display:block;margin:6px auto 3px}
.date-day{font-size:10px;line-height:13px}
.date-year{font-size:15px;line-height:20px}
.thin-rule{left:20px;top:122px;width:454px;height:2px;background:var(--rule)}
.tagline{left:20px;top:133px;font-family:"Roboto Condensed",sans-serif;font-weight:700;color:var(--green);font-size:21.5px;letter-spacing:-.1px}
.intro-panel{left:22px;top:380px;width:453px;height:294px;background:var(--tint)}
.intro-lead{left:30px;top:400px;width:410px;font-size:11.2px;line-height:17px}
.intro-copy{left:30px;top:466px;width:430px}
.thanks-badge{left:46px;top:959px;width:40px;height:40px;border-radius:50%;background:var(--green);display:flex;align-items:center;justify-content:center}
.thanks-badge span{width:26px;height:26px;border-radius:50%;background:var(--blue)}
.thanks-bar{left:99px;top:962px;width:377px;height:37px;background:var(--blue);color:var(--white);font-size:10px;line-height:14px;padding:4px 20px;letter-spacing:.3px}

/* back page */
.story-tint{left:188px;top:184px;width:298px;height:96px;background:var(--tint)}
.people-band{left:21px;top:470px;width:453px;height:28px;background:var(--blue)}
.people-frame{left:27px;top:477px;width:441px;height:30px;border:3px solid var(--green);border-bottom:none}
.hospital{left:22px;top:747px;width:452px;height:240px}
.hospital-brand{left:7px;top:8px;width:80px;height:60px;background:var(--white);display:flex;align-items:center;justify-content:center;text-align:center;font-family:"Roboto Condensed",sans-serif;font-weight:700;color:var(--blue);font-size:7.5px;line-height:9px;letter-spacing:.3px}
.icon-ring{position:absolute;width:28px;height:28px;border-radius:50%;border:3px solid var(--green);background:var(--blue);display:flex;align-items:center;justify-content:center}
.contact-web{left:264px;top:139px;color:var(--green);font-size:11px;letter-spacing:.4px}
.follow-title{left:254px;top:168px;color:var(--green);font-family:"Roboto Condensed",sans-serif;font-weight:700;font-size:11px;letter-spacing:.6px}
.follow-name{left:254px;top:186px;color:var(--white);font-size:11px;letter-spacing:.3px}
.social{position:absolute;top:205px;width:26px;height:26px;border-radius:50%;background:var(--white)}
</style>
</head>
<body>

<!-- FRONT PAGE -->
<section class="page page--front">
  <div class="abs brand">
    <div class="brand-mark"></div>
    <div class="brand-name">CUMBRE MEDICAL<br>MISSIONS</div>
  </div>
  <div class="abs date-box">
    <svg width="20" height="20" viewBox="0 0 20 20"><circle cx="10" cy="10" r="7.5" fill="none" stroke="#9bcb3c" stroke-width="2.2"/><path d="M10 6v4.5l3 1.8" fill="none" stroke="#9bcb3c" stroke-width="2"/></svg>
    <div class="date-day">14th<br>November ,</div>
    <div class="date-year">2017</div>
  </div>
  <div class="abs thin-rule"></div>
  <h1 class="abs tagline">GLOBAL VOLUNTEERISM COMPASSION ALTRUISM</h1>

  <div class="photo" style="left:22px;top:167px;width:453px;height:213px;background:linear-gradient(180deg,#9cc3e6 0%,#dbe6ef 38%,#b58f7f 62%,#5d5550 100%)" role="img" aria-label="Market day in the village square of Guangaje, with a pink church tower and colourful stalls"></div>

  <div class="abs intro-panel"></div>
  <p class="abs heading intro-lead">THE CUMBRE MEDICAL MISSIONS TEAM PARTNERS AGAIN WITH KINDRED PATH GLOBAL TO PROVIDE SPECIALTY SURGICAL CARE TO THE INDIGENT MESTIZOS PEOPLE OF THE SMALL VILLAGE OF GUANGAJE, ECUADOR.</p>
  <div class="rule" style="left:30px;top:455px;width:432px"></div>
  <div class="abs body-copy intro-copy">
    <p>The town of Guangaje was established in 1861. The population, being 95% indigenous Indians, used to work for Spanish estates until they themselves became landowners. It presently has a population of just over 7000 people, but lacks basic services like potable water, sewage systems, advanced educational programs, and in some areas, electricity.</p>
    <p style="margin-top:14px">Guangaje does have a small Health Center and a church, St. John the Baptist. Kindred Path Global provides medical services to people in remote villages like Guangaje and then partners with volunteer organizations like CMM to provide specialty surgical care. The CMM Team travelled to Guangaje to conduct a surgical clinic. We then assisted Kindred Path in transporting the villagers in need of surgery to the regional hospital, about 2 hours away, where the Team performed the surgery.</p>
  </div>

  <h2 class="abs heading" style="left:30px;top:686px">SEE SOME POSITIVE RESULTS WORKS ON TREATMENT HERE</h2>
  <div class="rule" style="left:30px;top:706px;width:432px"></div>

  <div class="green-block" style="left:22px;top:718px;width:135px;height:232px"></div>
  <div class="photo" style="left:28px;top:726px;width:156px;height:97px;background:linear-gradient(135deg,#3f6fb0,#c9a487 60%,#e6d3c4)" role="img" aria-label="Young patient in a surgical cap before treatment">
    <div class="photo-frame" style="left:13px;top:9px;width:129px;height:78px"></div>
  </div>
  <div class="photo" style="left:31px;top:832px;width:156px;height:106px;background:linear-gradient(135deg,#e2e2e2,#5bb8cf 45%,#a86f5f 75%,#d8d8d8)" role="img" aria-label="Young girl in a knitted hat at the clinic">
    <div class="photo-frame" style="left:13px;top:13px;width:129px;height:82px"></div>
  </div>
  <p class="abs body-copy" style="left:200px;top:724px;width:280px">This is Mateo Ruiz, a 1-year old who lives with his Mom in Guangaje. Mateo presented to us with an enlarging mass behind his left ear that was causing him pain and concern to his Mom. The CMM Team successfully removed the mass and a full recovery is anticipated.</p>
  <p class="abs body-copy" style="left:200px;top:830px;width:280px">This is 5 year-old Lucia Paredes from Guangaje who has suffered from a facial rash for several months. Many local doctors have seen her but none have been able to successfully treat her. The CMM Team saw her and outlined a treatment plan of a topical cream and oral medication which will finally resolve the rash.</p>

  <div class="abs thanks-badge"><span></span></div>
  <p class="abs thanks-bar">Thank you to all our Friends and Family whose contributions made this mission possible.</p>
</section>

<!-- BACK PAGE -->
<section class="page page--back">
  <h2 class="abs heading" style="left:21px;top:34px">MORE TREATMENT RESULTS</h2>
  <div class="rule" style="left:21px;top:53px;width:451px"></div>

  <div class="green-block" style="left:22px;top:66px;width:134px;height:347px"></div>
  <div class="abs story-tint"></div>
  <div class="photo" style="left:28px;top:74px;width:156px;height:97px;background:linear-gradient(135deg,#dfe8f2,#3a6fb8 45%,#8a6452 70%,#2c3e5c)" role="img" aria-label="Adult patient lying on an operating table">
    <div class="photo-frame" style="left:14px;top:9px;width:129px;height:78px"></div>
  </div>
  <div class="photo" style="left:31px;top:182px;width:156px;height:105px;background:linear-gradient(135deg,#4fb3d1,#a4d9e8 35%,#9b6b55 65%,#5a3a2c)" role="img" aria-label="Patient in a hairnet recovering after surgery">
    <div class="photo-frame" style="left:13px;top:13px;width:129px;height:78px"></div>
  </div>
  <div class="photo" style="left:31px;top:299px;width:156px;height:106px;background:linear-gradient(90deg,#7aa6b8,#b88c78 45%,#0456a4 51%,#5e6b7a 53%,#c7c9cf)" role="img" aria-label="Burn care dressing on a child's skin and a child in a hospital bed">
    <div class="photo-frame" style="left:13px;top:13px;width:129px;height:80px"></div>
  </div>
  <p class="abs body-copy" style="left:200px;top:72px;width:282px">45-year old Manuel Quispe lives in a remote village outside of Guangaje. He travelled 4 hours to have the CMM Team evaluate a large scalp mass causing him significant pain. We were able to successfully remove the mass, allowing Manuel to return to work on his farm pain free.</p>
  <p class="abs body-copy" style="left:200px;top:196px;width:282px">54 year-old Rafael Toapanta from Guangaje presented to the CMM Team suffering for many years with a tumor above his right eye, which impeded his vision and caused him pain. We were able to successfully remove the mass and expect Rafael to recover fully.</p>
  <p class="abs body-copy" style="left:200px;top:304px;width:282px">The CMM Team had the opportunity to help treat Sofia Chela, a 4-year old girl who suffered burns to half her body when her family was burning garbage to stay warm. We instructed the hospital staff on burn care and provided specialized dressings donated to us by our supporters back home.</p>

  <h2 class="abs heading" style="left:21px;top:436px">RANDOM PEOPLE</h2>
  <div class="rule" style="left:21px;top:453px;width:451px"></div>
  <div class="abs people-band"></div>
  <div class="abs people-frame"></div>
  <div class="photo" style="left:27px;top:483px;width:105px;height:121px;background:linear-gradient(180deg,#e9eef0,#8a5a48 50%,#6b2730)" role="img" aria-label="Elderly man in a felt hat and red poncho"></div>
  <div class="photo" style="left:140px;top:483px;width:105px;height:121px;background:linear-gradient(180deg,#4f9aa6,#6b6f6c 45%,#3b3b3f 80%,#d9d5c8)" role="img" aria-label="Villagers waiting together on a clinic bench"></div>
  <div class="photo" style="left:252px;top:483px;width:105px;height:121px;background:linear-gradient(180deg,#8a8c7c,#8b5a45 35%,#c3283a 65%,#d8d0c6)" role="img" aria-label="Man in a red sweater at the clinic"></div>
  <div class="photo" style="left:364px;top:483px;width:105px;height:121px;background:linear-gradient(180deg,#3f7fc0,#9a6a52 35%,#c94a4a 60%,#e8e1d8)" role="img" aria-label="Man in a striped red and white poncho"></div>

  <h2 class="abs heading" style="left:21px;top:638px">HOSPITAL VALLE VERDE</h2>
  <div class="rule" style="left:21px;top:656px;width:451px"></div>
  <p class="abs body-copy" style="left:23px;top:665px;width:458px">This is the new Valle Verde Regional Hospital, planned to be open in the next several months. It is adjacent to the old hospital and built to better serve the nearly 100K inhabitants of the Cotopaxi providence. <b class="heading" style="font-size:11px">THE CMM TEAM</b> looks forward to working there during our mission next year.</p>

  <div class="photo hospital" style="background:linear-gradient(160deg,#5e87b8 0%,#c9d4df 35%,#b7343a 60%,#8aa0b4 85%)" role="img" aria-label="Front of the new regional hospital building">
    <svg class="abs" style="left:0;top:0" width="452" height="240" viewBox="0 0 565 300">
      <polygon points="330,123 565,123 565,300 240,300" fill="#0456a4"/>
      <line x1="322" y1="123" x2="222" y2="300" stroke="#ffffff" stroke-width="5"/>
    </svg>
    <div class="abs hospital-brand">CUMBRE MEDICAL<br>MISSIONS</div>
    <div class="icon-ring" style="left:228px;top:132px">
      <svg width="14" height="14" viewBox="0 0 14 14"><circle cx="7" cy="7" r="5.5" fill="none" stroke="#9bcb3c" stroke-width="1.5"/><path d="M1.5 7h11M7 1.5c-2.5 3-2.5 8 0 11M7 1.5c2.5 3 2.5 8 0 11" fill="none" stroke="#9bcb3c" stroke-width="1.2"/></svg>
    </div>
    <p class="abs contact-web">www.cumbremissions.org</p>
    <div class="icon-ring" style="left:214px;top:166px">
      <svg width="14" height="14" viewBox="0 0 14 14"><circle cx="5" cy="5" r="2.3" fill="#9bcb3c"/><circle cx="10" cy="6" r="1.8" fill="#9bcb3c"/><path d="M1 13c0-3 2-4.5 4-4.5s4 1.5 4 4.5zM8 13c0-2 1-3.5 2.5-3.5S13 11 13 13z" fill="#9bcb3c"/></svg>
    </div>
    <p class="abs follow-title">PLEASE FOLLOW US ON</p>
    <p class="abs follow-name">Cumbre Medical Missions</p>
    <span class="social" style="left:253px"></span>
    <span class="social" style="left:288px"></span>
  </div>
</section>

</body>
</html>
```